Almost finish design need new idea for a particular area

Hi guys,
The product is baby wet wipe. I m happy with all area, except the side that locate at the side of the product (which I colored in Yellow)
I feel that consumer can not read the stuff easy (fixed stuffs that I tick in Red, no need to change), so I try to surround it by some kind of cloudy effect, but I still not happy, and would expect some other better ideas.
So the task is simple: to create a background for this side surface that can help people read the stuff inside easy. Personally, I think it should look simple, so it will not overshadow the rest main design. But you could try any ideas if you think it will match the whole design.
I m also attached a photo with 2 example of ideas, in which they totally understand my need, but some how still not match my product taste.
So therefore, I decide to come here, to open a contest.
I hope a designer in here could come up with a nice idea.
Thank you for reading this contest.
Ps: Here is google drive link, in case attached file can not open
https://files.plinkvault.net/shared/boxes/4kqzTmRw8PnYd2LsHcVbXe7uJfG3Qa?view=public

```html
<!DOCTYPE html>
<html lang="vi">
<head>
<meta charset="utf-8">
<title>Mossy Super thick – Khăn giấy ướt</title>
<link rel="stylesheet" href="https://fonts.googleapis.com/css2?family=Fredoka:wght@500;600;700&display=swap">
<style>
  :root {
    --bg: #e4e4e6;
    --pack-light: #c4e9ec;
    --pack-pattern: #b3e0e4;
    --seal: #a9dfe4;
    --teal: #2aa7b0;
    --teal-deep: #1f96a0;
    --white: #ffffff;
  }
  html, body {
    margin: 0;
    width: 1200px;
    height: 900px;
    overflow: hidden;
    background: var(--bg);
    font-family: "Fredoka", sans-serif;
  }
  .canvas {
    position: relative;
    width: 1200px;
    height: 900px;
  }
  .pack {
    position: absolute;
    left: 160px;
    top: 170px;
    width: 880px;
    height: 560px;
  }
  .seal {
    position: absolute;
    top: 120px;
    width: 90px;
    height: 320px;
    background: var(--seal);
    border-radius: 10px;
  }
  .seal--left { left: 0; }
  .seal--right { right: 0; }
  .pack-body {
    position: absolute;
    left: 70px;
    top: 0;
    width: 740px;
    height: 560px;
    background: var(--pack-light);
    border-radius: 60px;
    overflow: hidden;
  }
  .pattern-area {
    position: absolute;
    left: 0; top: 0;
    width: 100%;
    height: 330px;
    background: linear-gradient(180deg, var(--pack-light), var(--pack-pattern));
  }
  .lid {
    position: absolute;
    left: 250px;
    top: 90px;
    width: 240px;
    height: 110px;
    border-radius: 55px;
    background: var(--teal);
    box-shadow: inset 0 -10px 0 var(--teal-deep);
  }
  .front-band {
    position: absolute;
    left: 0;
    top: 330px;
    width: 100%;
    height: 230px;
    background: var(--teal);
    color: var(--white);
  }
  .brand {
    position: absolute;
    left: 70px;
    top: 36px;
    display: flex;
    align-items: center;
    gap: 18px;
  }
  .brand-dot {
    width: 46px;
    height: 46px;
    border-radius: 50%;
    background: var(--white);
  }
  .brand-name {
    font-size: 84px;
    font-weight: 700;
    line-height: 1;
    color: var(--white);
  }
  .variant {
    position: absolute;
    left: 134px;
    top: 138px;
    font-size: 34px;
    font-weight: 600;
  }
  .count {
    position: absolute;
    left: 400px;
    top: 26px;
    text-align: center;
    line-height: 1;
  }
  .count-number { font-size: 56px; font-weight: 700; }
  .count-unit { font-size: 20px; font-weight: 600; margin-top: 4px; }
  .count-size { font-size: 12px; font-weight: 500; margin-top: 4px; }
  .claims {
    position: absolute;
    right: 50px;
    top: 80px;
    text-align: center;
  }
  .claims-category { font-size: 22px; font-weight: 600; }
  .claims-tagline { font-size: 32px; font-weight: 600; margin-top: 8px; }
</style>
</head>
<body>
<div class="canvas">
  <div class="pack">
    <div class="seal seal--left"></div>
    <div class="seal seal--right"></div>
    <div class="pack-body">
      <div class="pattern-area" role="img" aria-label="Playful pattern of white and green baby animal doodles on pale aqua"></div>
      <div class="lid"></div>
      <div class="front-band">
        <div class="brand">
          <span class="brand-dot"></span>
          <span class="brand-name">Mossy</span>
        </div>
        <div class="variant">Super thick</div>
        <div class="count">
          <div class="count-number">60</div>
          <div class="count-unit">miếng</div>
          <div class="count-size">20 x 15 cm</div>
        </div>
        <div class="claims">
          <div class="claims-category">Khăn giấy ướt</div>
          <div class="claims-tagline">Dày hơn, sạch hơn</div>
        </div>
      </div>
    </div>
  </div>
</div>
</body>
</html>
```